Real Estate For Sale Signage

I'm an independent agent in Lismore NSW Australia with high standards and looking for a catching 'For Sale'sign board.
I like classy, elegant, stylish and simple best.
My colours are red, white and black.
I don't have a logo or other font designs I need to stick to. I like the concept of a house or real estate design.
Before I created this project I played around on publisher and created the PDF attached. I'm not sold on it, but I don't mind the way the name has been layed out. Originally I had a white background with black & red font.
Fancy fonts for my name would be nice, but must not be busy.
Updates

Just wanted to advise that I have updated my brief and used the tools available to help get my ideas through.

Thank you for your work and time.

Kind regards
Marella

Industry/Entity Type

Real Estate

Requirements
Must have
• For Sale
Marella Quint Real Estate (must stand out)
0400 517 382 (must stand out)
17 Tallowood Street North Lismore
www.marellaquintrealestate.com.au

```html
<!DOCTYPE html>
<html lang="en">
<head>
<meta charset="utf-8">
<title>Marella Quint Real Estate – For Sale Sign</title>
<link rel="stylesheet" href="https://fonts.googleapis.com/css2?family=Crimson+Text:ital,wght@1,600;1,700&family=Open+Sans:wght@600;700;800&display=swap">
<style>
  :root {
    --red-deep: #a5161b;
    --red-main: #c8202a;
    --red-bright: #e0313a;
    --rule-light: #f4c9cb;
    --black-band: #1c1c1c;
    --panel-pale: #f1f1f1;
    --white: #ffffff;
    --ink: #111111;
    --photo-sky: #2f7fd1;
    --photo-roof: #8c8f93;
    --photo-brick: #7a4d3c;
    --photo-garden: #5a8a3a;
  }
  html, body {
    margin: 0;
    padding: 0;
    overflow: hidden;
    background: var(--white);
  }
  .sign {
    position: relative;
    width: 848px;
    height: 1200px;
    overflow: hidden;
    background: var(--panel-pale);
  }
  .sign svg { display: block; }
  .headline-lead {
    font-family: "Open Sans", Arial, sans-serif;
    font-weight: 800;
    font-size: 80px;
    fill: var(--white);
  }
  .headline {
    font-family: "Open Sans", Arial, sans-serif;
    font-weight: 800;
    font-size: 260px;
    fill: var(--white);
    letter-spacing: -4px;
  }
  .agency-name {
    font-family: "Open Sans", Arial, sans-serif;
    font-weight: 700;
    font-size: 72px;
    fill: var(--white);
  }
  .web-address {
    font-family: "Crimson Text", Georgia, serif;
    font-style: italic;
    font-weight: 700;
    font-size: 62px;
    fill: var(--ink);
  }
  .booking-label {
    font-family: "Open Sans", Arial, sans-serif;
    font-weight: 700;
    font-size: 36px;
    fill: var(--red-deep);
    letter-spacing: 1px;
  }
  .booking-phone {
    font-family: "Open Sans", Arial, sans-serif;
    font-weight: 700;
    font-size: 80px;
    fill: var(--red-deep);
    letter-spacing: 1px;
  }
  .street-address {
    font-family: "Open Sans", Arial, sans-serif;
    font-weight: 600;
    font-size: 26px;
    fill: var(--ink);
  }
</style>
</head>
<body>
<main class="sign">
  <svg width="848" height="1200" viewBox="0 0 848 1200" xmlns="http://www.w3.org/2000/svg">
    <defs>
      <linearGradient id="house-photo-tones" x1="0" y1="0" x2="0.3" y2="1">
        <stop offset="0" stop-color="var(--photo-sky)"/>
        <stop offset="0.22" stop-color="var(--photo-roof)"/>
        <stop offset="0.6" stop-color="var(--photo-brick)"/>
        <stop offset="1" stop-color="var(--photo-garden)"/>
      </linearGradient>
      <linearGradient id="sale-band-fill" x1="0" y1="0" x2="1" y2="0">
        <stop offset="0" stop-color="var(--red-deep)"/>
        <stop offset="1" stop-color="var(--red-bright)"/>
      </linearGradient>
      <filter id="headline-shadow" x="-10%" y="-10%" width="120%" height="130%">
        <feDropShadow dx="6" dy="8" stdDeviation="5" flood-color="#2a0000" flood-opacity="0.7"/>
      </filter>
    </defs>

    <polygon class="house-photo" role="img" aria-label="Photograph of a large brick family home with arched windows, grey roof and landscaped front garden under a blue sky"
             points="0,0 848,0 848,238 0,530" fill="url(#house-photo-tones)"/>

    <polygon class="band-white-top" points="0,530 848,238 848,263 0,555" fill="var(--white)"/>
    <polygon class="band-sale" points="0,555 848,263 848,540 0,832" fill="url(#sale-band-fill)"/>
    <polygon class="band-accent" points="0,832 848,540 848,560 0,852" fill="var(--rule-light)"/>
    <polygon class="band-agency" points="0,852 848,560 848,740 0,1032" fill="var(--black-band)"/>
    <polygon class="band-web" points="0,1032 848,740 848,880 0,1172" fill="var(--white)"/>

    <text class="headline-lead" x="20" y="640" transform="rotate(-19 20 640)">FOR</text>
    <text class="headline" x="130" y="800" transform="rotate(-19 130 800)" filter="url(#headline-shadow)">SALE</text>

    <text class="agency-name" x="26" y="1010" transform="rotate(-19 26 1010)">MARELLA QUINT</text>
    <text class="agency-name" x="320" y="831" transform="rotate(-19 320 831)">REAL ESTATE</text>

    <text class="web-address" x="21" y="1143" transform="rotate(-19 21 1143)">www.marellaquintrealestate.com.au</text>

    <text class="booking-label" x="600" y="1058" text-anchor="middle">FOR BOOKING CALL</text>
    <text class="booking-phone" x="816" y="1138" text-anchor="end">0400 517 382</text>
    <text class="street-address" x="816" y="1182" text-anchor="end">17 Tallowood Street North Lismore</text>
  </svg>
</main>
</body>
</html>
```